Kelvard Engineers: Why you should hire us keepsake

New design. Open to plastic cards. We are an engineering firm that designs cell phone towers and commercial buildings. Please check out our website www.kelvardeng.example for more details. We want people to remember our card and for it to be useful if possible. We want the same look and feel on these cards to be translated to other marketing material we may need such as brochures.

Target Market(s)

Architects, Developers and Telecommunication Carriers

Industry/Entity Type

Engineering

Contact Information for Business Card

Card with our company colors, logo, and innovative design with elements related to our industry.

Font styles to use
Sans Serif

Colors
9bcb3c
abd036
0255a3

Requirements
Must have
• Sleek and hip design
Nice to have
• Bright lime green and navy coloring that pops with an innovative design.
Should not have
• A basic and boring design

```html
<!DOCTYPE html>
<html lang="en">
<head>
<meta charset="utf-8">
<title>Kelvard Engineers – Business Card</title>
<link href="https://fonts.googleapis.com/css2?family=Roboto:wght@400;700;900&family=Roboto+Condensed:wght@700&display=swap" rel="stylesheet">
<style>
  :root {
    --stage: #2a2a2c;
    --card-dark: #1d1e1f;
    --card-light: #f4f4f2;
    --lime: #3cf21c;
    --navy: #0255a3;
    --white: #ffffff;
    --ink-grey: #555759;
    --divider: #8a8a8a;
  }
  * { margin: 0; padding: 0; box-sizing: border-box; }
  html, body {
    width: 1200px; height: 900px; overflow: hidden;
    background: var(--stage);
    font-family: "Roboto", Arial, sans-serif;
  }
  .canvas {
    width: 1200px; height: 900px;
    display: flex; flex-direction: column;
    align-items: center; justify-content: center; gap: 40px;
  }
  .card {
    width: 660px; height: 377px;
    position: relative;
    box-shadow: 0 14px 30px rgba(0,0,0,.45);
  }
  /* Front */
  .card--front {
    background: var(--card-dark);
    display: flex; flex-direction: column; align-items: center; justify-content: center;
  }
  .brand-name {
    font-family: "Roboto", Arial, sans-serif;
    font-weight: 900;
    font-size: 96px;
    letter-spacing: -2px;
    color: var(--lime);
    line-height: 1;
    margin-bottom: 30px;
  }
  .tagline {
    display: flex; align-items: center; gap: 10px;
    font-weight: 700; font-size: 17px; letter-spacing: .5px;
    color: var(--lime);
  }
  .tagline__rule { width: 40px; height: 1px; background: var(--navy); }
  .locations {
    margin-top: 6px;
    font-size: 16px; letter-spacing: 1px;
    color: var(--white);
  }
  /* Back */
  .card--back {
    background: var(--card-light);
    display: flex; align-items: center;
  }
  .person-name {
    width: 355px; text-align: right; padding-right: 26px;
    font-family: "Roboto Condensed", Arial, sans-serif;
    font-weight: 700; font-size: 27px;
    color: var(--lime);
    text-transform: uppercase;
  }
  .divider {
    width: 2px; height: 96px;
    background: linear-gradient(var(--card-light), var(--divider), var(--card-light));
  }
  .contact-list { list-style: none; padding-left: 22px; }
  .contact-list li {
    display: flex; align-items: center; gap: 10px;
    font-size: 17px; color: var(--ink-grey); line-height: 24px;
  }
  .contact-list svg { width: 14px; height: 14px; flex: none; fill: var(--lime); }
</style>
</head>
<body>
<main class="canvas">
  <section class="card card--front">
    <div class="brand-name">Kelvard</div>
    <div class="tagline">
      <span class="tagline__rule"></span>
      <span>MULTI-DISCIPLINE ENGINEERING</span>
      <span class="tagline__rule"></span>
    </div>
    <div class="locations">Ridgefield | Lakemont | Brookvale | Westhaven</div>
  </section>

  <section class="card card--back">
    <div class="person-name">Dana Holloway Reyes</div>
    <div class="divider"></div>
    <ul class="contact-list">
      <li>
        <svg viewBox="0 0 24 24" aria-hidden="true"><path d="M6.6 10.8a15 15 0 0 0 6.6 6.6l2.2-2.2c.3-.3.7-.4 1-.2 1.1.4 2.3.6 3.6.6.6 0 1 .4 1 1V20c0 .6-.4 1-1 1A17 17 0 0 1 3 4c0-.6.4-1 1-1h3.5c.6 0 1 .4 1 1 0 1.3.2 2.5.6 3.6.1.3 0 .7-.2 1z"/></svg>
        <span>555.014.7731</span>
      </li>
      <li>
        <svg viewBox="0 0 24 24" aria-hidden="true"><path d="M7 1h10a2 2 0 0 1 2 2v18a2 2 0 0 1-2 2H7a2 2 0 0 1-2-2V3a2 2 0 0 1 2-2zm0 3v14h10V4zm5 15.5a1 1 0 1 0 0 2 1 1 0 0 0 0-2z"/></svg>
        <span>555.019.2468</span>
      </li>
      <li>
        <svg viewBox="0 0 24 24" aria-hidden="true"><path d="M2 5h20v14H2zm2 2v.5l8 5 8-5V7l-8 5z"/></svg>
        <span>dreyes@kelvardeng.example</span>
      </li>
      <li>
        <svg viewBox="0 0 24 24" aria-hidden="true"><circle cx="12" cy="12" r="10"/></svg>
        <span>www.kelvardeng.example</span>
      </li>
    </ul>
  </section>
</main>
</body>
</html>
```